Martin Hale PA Card Logo

Current logo attached. Its 25 year old logo I have used. Looking for a new fresh elegant professional look/design for a law firm that has high net worth clientele and is estate planning business law firm. Firm mis in Palm Beach Florida.
One sided card linen stock white will be used. Logo section name section. Logo should include nice elegant design using the letter "M" perhapa (I am not wed to current font of the M on current logo.) Be creative there with logo design. My initials are MH.......color scheme I figure 3 tone... Raised Gold Foil, Blue name of firm = Martin Hale, P.A. My practice focus is Family and Business Asset Protection. My name is Martin M. Hale, Esq. Practice specialties include Asset Protection trusts, Business Succession Planning, LLC law, Estate Planning, Medicaid Planning (Maybe put those topics in bullets in a section of card. Bottom of card can be reserved smaller print address phone website and email address. Address section is not as important as logo and topics of practice on front. I foresee address section can be in dark blue. MY name and Topics dark blue as well.
Target Market(s)
affluent; business owners executives; wealth 2-10 million net worth
Industry/Entity Type
business law and estate planning
Contact Information for Business Card
White thick linen one sided

```html
<!DOCTYPE html>
<html lang="en">
<head>
<meta charset="utf-8">
<title>Martin Hale, P.A. – Business Card</title>
<link href="https://fonts.googleapis.com/css2?family=Cormorant+Garamond:wght@500&family=Montserrat:wght@300&family=PT+Sans+Narrow&family=Source+Sans+3:wght@400;700&display=swap" rel="stylesheet">
<style>
  :root {
    --backdrop: #eadbc6;
    --card: #f7f5f0;
    --navy: #1c2740;
    --gold: #c39a2a;
    --slate: #3f4a5e;
  }
  html, body {
    margin: 0;
    width: 721px;
    height: 1200px;
    overflow: hidden;
    background: var(--backdrop);
  }
  .canvas {
    position: relative;
    width: 721px;
    height: 1200px;
  }
  .card {
    position: absolute;
    left: 40px;
    top: 417px;
    width: 640px;
    height: 366px;
    background: var(--card);
    box-shadow: 0 6px 18px rgba(80, 60, 30, 0.18);
  }
  .brand-mark {
    position: absolute;
    left: 44px;
    top: 92px;
    width: 84px;
    height: 84px;
    border-radius: 50%;
    background: var(--gold);
  }
  .firm-name {
    position: absolute;
    left: 146px;
    top: 34px;
    margin: 0;
    font-family: "Cormorant Garamond", serif;
    font-weight: 500;
    font-size: 50px;
    line-height: 0.92;
    letter-spacing: 1px;
    color: var(--navy);
    text-transform: uppercase;
  }
  .tagline {
    position: absolute;
    left: 150px;
    top: 148px;
    margin: 0;
    font-family: "Montserrat", sans-serif;
    font-weight: 300;
    font-size: 13px;
    line-height: 1.35;
    letter-spacing: 2.4px;
    color: var(--slate);
    text-transform: uppercase;
  }
  .specialties {
    position: absolute;
    left: 382px;
    top: 168px;
    margin: 0;
    padding: 0;
    list-style: none;
    font-family: "PT Sans Narrow", sans-serif;
    font-size: 19px;
    line-height: 1.3;
    color: var(--navy);
  }
  .specialties li::before {
    content: "•";
    color: var(--gold);
    margin-right: 6px;
    font-size: 14px;
  }
  .contact {
    position: absolute;
    left: 60px;
    top: 238px;
    font-family: "Source Sans 3", sans-serif;
    font-size: 20px;
    line-height: 1.22;
    color: var(--navy);
  }
  .contact .person {
    font-weight: 700;
    font-size: 21px;
  }
</style>
</head>
<body>
<div class="canvas">
  <div class="card">
    <div class="brand-mark" aria-hidden="true"></div>
    <h1 class="firm-name">Martin<br>Hale, P.A.</h1>
    <p class="tagline">Family and Business<br>Asset Protection</p>
    <ul class="specialties">
      <li>Asset Protection trusts</li>
      <li>Business Succession Planning</li>
      <li>LLC law, Estate Planning</li>
      <li>Medicaid Planning</li>
    </ul>
    <div class="contact">
      <div class="person">Martin M. Hale</div>
      <div class="phone">561-555-0148</div>
      <div class="email">hale@palmestatelaw.com</div>
    </div>
  </div>
</div>
</body>
</html>
```